Professional and creatice Life Coach - Business Card design

I just relaunched my website and now i a need a correspoonding business card for my task as life coach. My website is www.tbalrond.com as reference. The compass is kind of a symbol for my work, as I help people navigate through their challenging phases in life. The business card should be colorful, but not too playful as I also adress business people. So it sould be creative, but professional (also to suport my other business as Management Consultant)

Target Market(s)

People who want to get teir problems resolved, in business, partnership and other personal realms

Industry/Entity Type

Life Coaching

Contact Information for Business Card

Front side should include Name, Phone number, Email, Website and address

Font styles to use
Sans Serif

Colors
add136

Requirements
Must have
• "Mag. Leopold Brantner" -> Name
"Energetische Praxis" -> Jobtitle (describing my profession as life coach)
colours and style should match my website www.tbalrond.com
Nice to have
• a compass as a symbol

```html
<!DOCTYPE html>
<html lang="de">
<head>
<meta charset="utf-8">
<title>Leopold Brantner – Visitenkarte</title>
<link href="https://fonts.googleapis.com/css2?family=Merriweather:wght@300;400&display=swap" rel="stylesheet">
<style>
  :root {
    --stage: #cfe03a;
    --card: #ffffff;
    --brand: #a8c72e;
    --ink: #4a4a4a;
    --icon: #555555;
  }
  * { margin: 0; padding: 0; box-sizing: border-box; }
  html, body { width: 1200px; height: 1200px; overflow: hidden; }
  body {
    background: var(--stage);
    position: relative;
    font-family: "Merriweather", Georgia, serif;
  }
  .card {
    position: absolute;
    top: 457px;
    width: 468px;
    height: 260px;
    background: var(--card);
  }
  .card--front { left: 78px; }
  .card--back { left: 653px; }

  .brand-mark {
    position: absolute;
    display: flex;
    flex-direction: column;
    align-items: center;
    gap: 8px;
    transform: translate(-50%, -50%);
    color: var(--brand);
    font-weight: 400;
  }
  .brand-mark__dot { border-radius: 50%; background: var(--brand); }
  .card--front .brand-mark { left: 96px; top: 139px; font-size: 18px; }
  .card--front .brand-mark__dot { width: 22px; height: 22px; }
  .card--back .brand-mark { left: 233px; top: 137px; font-size: 30px; gap: 12px; }
  .card--back .brand-mark__dot { width: 34px; height: 34px; }

  .name {
    position: absolute;
    right: 29px;
    top: 36px;
    font-size: 22px;
    font-weight: 300;
    color: var(--brand);
    white-space: nowrap;
  }
  .job-title {
    position: absolute;
    left: 0;
    width: 624px;
    text-align: center;
    top: 69px;
    font-size: 14.5px;
    font-weight: 300;
    color: var(--ink);
    letter-spacing: 0.2px;
    white-space: nowrap;
  }
  .contact {
    position: absolute;
    left: 222px;
    top: 113px;
    height: 103px;
    border-left: 1.5px solid var(--brand);
    list-style: none;
  }
  .contact__item {
    position: absolute;
    left: 14px;
    display: flex;
    align-items: flex-start;
    font-size: 11px;
    font-weight: 300;
    color: var(--brand);
    white-space: nowrap;
    line-height: 14px;
  }
  .contact__item svg {
    width: 15px; height: 15px;
    margin-right: 10px;
    flex: none;
    fill: none;
    stroke: var(--icon);
    stroke-width: 1.3;
  }
  .contact__item--phone { top: 1px; }
  .contact__item--web { top: 27px; }
  .contact__item--mail { top: 50px; }
  .contact__item--address { top: 77px; }
</style>
</head>
<body>
  <section class="card card--front">
    <div class="brand-mark">
      <span class="brand-mark__dot"></span>
      <span class="brand-mark__name">Brantner</span>
    </div>
    <h1 class="name">Mag. Leopold Brantner</h1>
    <p class="job-title">ENERGETISCHE PRAXIS</p>
    <ul class="contact">
      <li class="contact__item contact__item--phone">
        <svg viewBox="0 0 16 16"><path d="M4 1.5l2.5 3-1.5 1.5c.8 2 2.5 3.8 4.5 4.8l1.5-1.5 3 2.4-1.6 2.3C7.5 13.6 2.4 8.5 2 3.2z" fill="var(--icon)" stroke="none"/></svg>
        +43 664 3918042
      </li>
      <li class="contact__item contact__item--web">
        <svg viewBox="0 0 16 16"><circle cx="8" cy="8" r="6.5"/><ellipse cx="8" cy="8" rx="3" ry="6.5"/><path d="M1.5 8h13M2.5 4.8h11M2.5 11.2h11"/></svg>
        www.tbalrond.com
      </li>
      <li class="contact__item contact__item--mail">
        <svg viewBox="0 0 16 16"><rect x="1" y="3.5" width="14" height="9"/><path d="M1 3.5l7 5.5 7-5.5M1 12.5l5-4.5M15 12.5l-5-4.5"/></svg>
        leopold@brantner.one
      </li>
      <li class="contact__item contact__item--address">
        <svg viewBox="0 0 16 16"><path d="M1 8.5L8 2l7 6.5M3 7v7h3.8v-4h2.4v4H13V7M11.5 2.5v2.8" stroke-width="2"/></svg>
        <span>Lindenweg 12, 5020 Salzburg,<br>Österreich</span>
      </li>
    </ul>
  </section>

  <section class="card card--back">
    <div class="brand-mark">
      <span class="brand-mark__dot"></span>
      <span class="brand-mark__name">Brantner</span>
    </div>
  </section>
</body>
</html>
```